Unterstanding People Management, Compliance and the role of the Board

I have already and existing presentation but would like to have it made nicer and more appealing. I need to have the final version back no later than this COB CET Tuesday, 30 Jan24.
I would prefer to have all in green as further, two logos need to be added:

Kestrel Hill University and Alpine Directors Academy. For reference see an other PPP.

Target Market(s)

Board members

Colors

Designer to choose colors to be used in the design.

Requirements
Must have
• Appealing and easy to understand
Nice to have
• Add the logos from Kestrel Hill University and Alpine Directors Academy

```html
<!DOCTYPE html>
<html lang="de">
<head>
<meta charset="utf-8">
<title>People Management, Compliance und der VR – Präsentation</title>
<link rel="stylesheet" href="https://fonts.googleapis.com/css2?family=Arimo:wght@400;700&display=swap">
<style>
:root{
  --stage:#808080;
  --green-deep:#0a5219;
  --green-mid:#0e6a24;
  --green:#0c8a3b;
  --green-tag:#0b7046;
  --teal:#037052;
  --yellow:#fbbf00;
  --ink:#222;
  --ink-soft:#555;
  --red:#d6312b;
  --white:#fff;
}
*{box-sizing:border-box;margin:0;padding:0}
html,body{width:1031px;height:1200px;overflow:hidden}
body{background:var(--stage);font-family:"Arimo",Arial,sans-serif;position:relative;color:var(--ink)}
.slide{position:absolute;width:438px;height:246px;background:var(--white);overflow:hidden;box-shadow:6px 8px 14px rgba(0,0,0,.35)}
.s1{left:65px;top:60px}.s2{left:526px;top:60px}
.s3{left:65px;top:326px}.s4{left:526px;top:326px}
.s5{left:65px;top:592px}.s6{left:526px;top:592px}
.s7{left:65px;top:858px}.s8{left:526px;top:858px}
.abs{position:absolute}
.brand{position:absolute;left:296px;top:9px;width:142px;height:30px;display:flex;align-items:center;gap:4px;padding:0 8px 0 7px;background:var(--white);font-size:5.4px;white-space:nowrap}
.brand .mark{width:7px;height:7px;background:var(--green-tag);flex:none}
.brand .uni{color:var(--ink)}
.brand .sep{width:.6px;height:15px;background:#999;margin:0 4px;flex:none}
.brand .academy{color:var(--red);font-weight:700;font-size:4.4px;line-height:5.2px;white-space:normal;width:40px}
.tag{position:absolute;left:0;height:8px;width:90px;background:var(--green-tag);color:var(--white);font-size:5.6px;line-height:8px;padding-left:44px}
.hex-field{position:absolute;right:0;bottom:0;width:190px;height:190px;background:radial-gradient(circle at 100% 100%,rgba(200,200,200,.45),rgba(235,235,235,.25) 55%,rgba(255,255,255,0) 75%)}
.foot{position:absolute;right:12px;bottom:10px;font-size:3.6px;color:#aaa}
.pageno{position:absolute;left:18px;bottom:10px;font-size:3.6px;color:#aaa}
.kicker{font-size:5.6px;color:#999;text-align:center}
.h-title{font-size:15.5px;text-align:center;line-height:18px;color:#333;letter-spacing:.1px}
.h-title .y{color:var(--yellow)}
.s1 .band{position:absolute;left:0;top:0;width:438px;height:177px;background:linear-gradient(160deg,var(--green-deep),var(--green-mid))}
.s1 .course{left:21px;top:19px;font-size:6px;color:var(--white)}
.s1 .course span{color:var(--yellow)}
.s1 h1{position:absolute;left:21px;top:38px;font-size:25px;line-height:27.5px;color:var(--yellow);font-weight:700}
.s1 .hexes{position:absolute;right:0;top:88px;width:230px;height:158px;background:linear-gradient(200deg,#cfcfcf,#8b8b8b 55%,#d9d9d9);clip-path:polygon(100% 0,100% 100%,0 100%,30% 60%,60% 25%)}
.s1 .author{left:21px;top:200px;font-size:4.6px;line-height:9px}
.s1 .author b{color:var(--ink)}
.s1 .author .role{color:var(--green)}
.s1 .author .copy{color:#999}
.s2 .field{position:absolute;left:117px;top:0;right:0;bottom:0;background:var(--green)}
.s2 .num{position:absolute;left:30px;top:46px;width:169px;height:154px;background:var(--yellow);color:var(--white);font-size:110px;line-height:154px;text-align:center}
.s2 .combs{position:absolute;right:0;top:0;width:80px;height:105px;background:linear-gradient(210deg,var(--yellow),#ffe27a 60%,rgba(255,226,122,0));clip-path:polygon(40% 0,100% 0,100% 100%,80% 100%,45% 55%)}
.s2 .sub{left:227px;top:109px;font-size:7px;color:var(--white)}
.s2 .chapter{left:227px;top:121px;font-size:15.5px;line-height:19px;font-weight:700;color:var(--yellow)}
.law{position:absolute;left:44px;top:74px;width:360px;font-size:5.4px;color:var(--ink-soft)}
.law .art{font-weight:700;color:var(--ink);font-size:6px;position:relative;padding-left:11px}
.law .art:before{content:"";position:absolute;left:0;top:0;border-left:6px solid var(--yellow);border-top:3.5px solid transparent;border-bottom:3.5px solid transparent}
.law .lead{margin:4px 0 4px 15px;color:var(--ink)}
.law .lead b{font-weight:700}
.law ol{list-style:none;margin-left:15px}
.law li{display:flex;line-height:10.8px}
.law li .n{width:12px;color:var(--yellow);flex:none}
.law .hl{color:var(--yellow);font-weight:700;font-size:7px}
.law .more{margin-left:15px}
.s6 .focus-list{position:absolute;left:305px;top:47px;font-size:5.6px;line-height:11px;font-weight:700;color:var(--green)}
.s6 .law{left:44px;top:74px;width:345px}
.s7 .ttl{position:absolute;left:44px;top:45px;font-size:15px;line-height:18px}
.s7 .ttl b{color:var(--green-tag)}
.s7 .ttl span{color:#333}
.s7 .cases{position:absolute;left:41px;top:104px;list-style:none;font-size:6.2px;line-height:11.5px;color:var(--ink-soft)}
.s7 .cases i{font-style:normal;color:var(--yellow);display:inline-block;width:9px}
.s8{background:var(--teal);color:var(--white);text-align:center}
.s8 .kicker{color:#ccc;position:absolute;top:22px;width:100%}
.s8 .rel{position:absolute;top:33px;width:100%;font-size:15px;color:var(--yellow)}
.s8 .sc{position:absolute;top:84px;width:100%;font-size:10.5px;color:#9ab9a9}
.s8 blockquote{position:absolute;top:102px;left:0;width:100%;font-size:16px;line-height:29.5px;font-weight:700}
.s8 blockquote span{color:var(--yellow)}
.s8 .by{position:absolute;top:195px;width:100%;font-size:6px;color:var(--yellow)}
.s8 .foot,.s8 .pageno{color:#9bc1b0}
</style>
</head>
<body>

<section class="slide s1">
  <div class="band"></div>
  <p class="abs course">Kestrel Hill University <span>Public Corporate Governance – VR CAS</span></p>
  <h1>Das Zusammenspiel<br>zwischen People<br>Management,<br>Compliance und dem VR</h1>
  <div class="hexes" role="img" aria-label="Dekoratives Wabenmuster in Grautönen"></div>
  <div class="brand"><span class="mark"></span><span class="uni">Kestrel Hill University</span><span class="sep"></span><span class="academy">Alpine Directors Academy</span></div>
  <p class="abs author"><b>Mirela Hausmann-Vogt</b><br><span class="role">Rechtsanwältin | LL.M. | certified board member</span><br><span class="copy">© Copyright 2024</span></p>
</section>

<section class="slide s2">
  <div class="field"></div>
  <div class="combs" role="img" aria-label="Dekoratives Wabenmuster in Gelbtönen"></div>
  <div class="num">1</div>
  <div class="brand"><span class="mark"></span><span class="uni">Kestrel Hill University</span><span class="sep"></span><span class="academy">Alpine Directors Academy</span></div>
  <p class="abs sub">Compliance</p>
  <p class="abs chapter">GRUNDLAGEN UND<br>RECHTSRAHMEN</p>
</section>

<section class="slide s3">
  <div class="hex-field" role="img" aria-label="Dezentes Wabenmuster in Hellgrau"></div>
  <div class="brand"><span class="mark"></span><span class="uni">Kestrel Hill University</span><span class="sep"></span><span class="academy">Alpine Directors Academy</span></div>
  <div class="tag" style="top:31px">Compliance</div>
  <div class="law">
    <p class="art">Art. 716a</p>
    <p class="lead"><b>Der Verwaltungsrat</b> hat folgende <b>unübertragbare und unentziehbare</b> Aufgaben:</p>
    <ol>
      <li><span class="n">1.</span><span>die <span class="hl">Oberleitung</span> der Gesellschaft und die Erteilung der nötigen Weisungen;</span></li>
      <li><span class="n">2.</span><span>die Festlegung der Organisation;</span></li>
      <li><span class="n">3.</span><span>die Ausgestaltung des Rechnungswesens, der Finanzkontrolle sowie der Finanzplanung, sofern diese für die Führung der Gesellschaft notwendig ist;</span></li>
      <li><span class="n">4.</span><span>die Ernennung und Abberufung der mit der Geschäftsführung und der Vertretung betrauten Personen;</span></li>
      <li><span class="n">5.</span><span><span class="hl">die Oberaufsicht über die mit der Geschäftsführung betrauten Personen</span>, namentlich im Hinblick auf die Befolgung der <span class="hl">Gesetze, Statuten, Reglemente und Weisungen;</span></span></li>
      <li><span class="n">6.</span><span>die Erstellung des Geschäftsberichtes sowie die Vorbereitung der Generalversammlung und die Ausführung ihrer Beschlüsse;</span></li>
    </ol>
    <p class="more">…</p>
  </div>
  <p class="pageno">6</p>
  <p class="foot">© Corporate Governance, M. Hausmann-Vogt, 2023</p>
</section>

<section class="slide s4">
  <div class="hex-field" role="img" aria-label="Dezentes Wabenmuster in Hellgrau"></div>
  <div class="brand"><span class="mark"></span><span class="uni">Kestrel Hill University</span><span class="sep"></span><span class="academy">Alpine Directors Academy</span></div>
  <div class="tag" style="top:31px;padding:0"></div>
  <p class="abs kicker" style="top:32px;width:100%">Compliance</p>
  <h2 class="abs h-title" style="top:42px;width:100%;font-weight:400">WIE WERDEN <span class="y">COMPLIANCE</span><br><span class="y">VERSTÖSSE</span> ENTDECKT</h2>
  <svg class="abs" style="left:0;top:0" width="438" height="246" viewBox="0 0 438 246" font-family="Arimo, Arial, sans-serif">
    <defs>
      <linearGradient id="arrowShade" x1="0" y1="0" x2="1" y2="1"><stop offset="0" stop-color="#9aa3b1"/><stop offset="1" stop-color="#4d5668"/></linearGradient>
    </defs>
    <path d="M176 103 C130 112 98 140 78 185 L70 182 L70 206 L88 191 L82 188 C101 146 132 119 176 103 Z" fill="url(#arrowShade)" stroke="#4d5668" stroke-width=".6"/>
    <path d="M264 103 C310 110 345 142 362 183 L355 185 L372 204 L376 180 L369 182 C350 137 314 108 264 103 Z" fill="url(#arrowShade)" stroke="#4d5668" stroke-width=".6"/>
    <g font-size="6" font-weight="700" fill="#444">
      <text x="141" y="96" text-anchor="middle">Ex-Mitarbeiter</text>
      <text x="108" y="113" text-anchor="middle">Medien</text>
      <text x="80" y="129" text-anchor="middle">Konkurrenz</text>
      <text x="163" y="128" text-anchor="middle">Ex-Partner</text>
      <text x="153" y="147" text-anchor="middle">Regulierungsbehörde</text>
      <text x="74" y="150" text-anchor="end">Vertragspartner</text>
      <text x="74" y="157" text-anchor="end" font-weight="400">Kunden</text>
      <text x="116" y="171" text-anchor="middle">Auditors</text>
      <text x="270" y="96" text-anchor="middle"><tspan>Reporting</tspan><tspan font-weight="400"> an Vorgesetzter</tspan></text>
      <text x="331" y="105">Funktion</text>
      <text x="331" y="114" font-weight="400">HR, Legal, Compliance –</text>
      <text x="331" y="123" font-weight="400">enger Kontakt und Austausch</text>
      <text x="270" y="133" text-anchor="middle">Whistleblowing-Line</text>
      <text x="270" y="142" text-anchor="middle" font-weight="400">gemäss Organisation</text>
      <text x="270" y="151" text-anchor="middle" font-weight="400">des Unternehmens</text>
      <text x="383" y="154" text-anchor="middle">Internal Audit</text>
      <text x="312" y="172" text-anchor="end">Interne</text>
      <text x="312" y="180" text-anchor="end">Untersuchung</text>
    </g>
    <text x="67" y="220" text-anchor="middle" font-size="11" fill="#333">EXTERN</text>
    <text x="376" y="220" text-anchor="middle" font-size="11" fill="#333">INTERN</text>
  </svg>
  <p class="pageno">33</p>
  <p class="foot">© Corporate Governance, M. Hausmann-Vogt, 2023</p>
</section>

<section class="slide s5">
  <div class="hex-field" role="img" aria-label="Dezentes Wabenmuster in Hellgrau"></div>
  <div class="brand"><span class="mark"></span><span class="uni">Kestrel Hill University</span><span class="sep"></span><span class="academy">Alpine Directors Academy</span></div>
  <div class="tag" style="top:31px;padding:0"></div>
  <p class="abs kicker" style="top:32px;width:210px;left:114px">Compliance</p>
  <h2 class="abs h-title" style="top:42px;left:0;width:420px;font-weight:400">UMGANG MIT <span class="y">COMPLIANCE VERSTÖSSEN</span><br>DURCH DIE UNTERNEHMUNG</h2>
  <svg class="abs" style="left:0;top:0" width="438" height="246" viewBox="0 0 438 246" font-family="Arimo, Arial, sans-serif">
    <rect x="46" y="91" width="7" height="7" fill="#e3e3e3"/>
    <text x="58" y="96.5" font-size="4.8" font-weight="700" fill="#333">Transparente Kommunikation?</text>
    <polygon points="171,90 267,90 267,110 314,110 219,129 123,110 171,110" fill="#e3e3e3"/>
    <g font-size="5.6" font-weight="700" fill="#333" text-anchor="middle">
      <text x="219" y="99">Je nach dem:</text>
      <text x="219" y="107">Sexuelle Übergriffe oder</text>
      <text x="219" y="115">Spesenvergehen…</text>
    </g>
    <path d="M201 147 A21 21 0 0 1 237 147" fill="none" stroke="var(--yellow)" stroke-width="1.4"/>
    <path d="M201 177 A21 21 0 0 0 237 177" fill="none" stroke="#333" stroke-width="1.4"/>
    <text x="219" y="160" text-anchor="middle" font-size="5.8" font-weight="700" fill="#333">Konsequenzen/</text>
    <text x="219" y="167" text-anchor="middle" font-size="5.8" font-weight="700" fill="#333">Sanktionen auf</text>
    <polygon points="65,156 142,156 142,149 155,167 142,184 142,177 65,177" fill="#e3e3e3"/>
    <text x="107" y="169" text-anchor="middle" font-size="6" font-weight="700" fill="#333">Schutz</text>
    <polygon points="370,156 297,156 297,149 284,167 297,184 297,177 370,177" fill="#e3e3e3"/>
    <text x="333" y="169" text-anchor="middle" font-size="6" font-weight="700" fill="#333">Signalfunktion</text>
    <line x1="27" y1="190" x2="412" y2="190" stroke="#333" stroke-width="1"/>
    <line x1="219" y1="183" x2="219" y2="190" stroke="#333" stroke-width="1"/>
    <g fill="none" stroke-width="1.2">
      <g stroke="#333">
        <path d="M16 200 A11 11 0 0 1 38 200"/><path d="M80 200 A11 11 0 0 1 102 200"/><path d="M144 200 A11 11 0 0 1 166 200"/><path d="M208 200 A11 11 0 0 1 230 200"/><path d="M273 200 A11 11 0 0 1 295 200"/><path d="M337 200 A11 11 0 0 1 359 200"/><path d="M401 200 A11 11 0 0 1 423 200"/>
      </g>
      <g stroke="var(--yellow)">
        <path d="M16 214 A11 11 0 0 0 38 214"/><path d="M80 214 A11 11 0 0 0 102 214"/><path d="M144 214 A11 11 0 0 0 166 214"/><path d="M208 214 A11 11 0 0 0 230 214"/><path d="M273 214 A11 11 0 0 0 295 214"/><path d="M337 214 A11 11 0 0 0 359 214"/><path d="M401 214 A11 11 0 0 0 423 214"/>
      </g>
    </g>
    <g font-size="6" font-weight="700" fill="#333" text-anchor="middle">
      <text x="27" y="210">«Täter»</text><text x="91" y="210">Organisation</text><text x="155" y="210">Prozesse</text><text x="219" y="210">Reglemente</text><text x="284" y="210">Schulung</text><text x="348" y="210">Kommunikation</text><text x="412" y="210">Dritte</text>
    </g>
  </svg>
  <p class="pageno">34</p>
  <p class="foot">© Corporate Governance, M. Hausmann-Vogt, 2023</p>
</section>

<section class="slide s6">
  <div class="hex-field" role="img" aria-label="Dezentes Wabenmuster in Hellgrau"></div>
  <div class="brand"><span class="mark"></span><span class="uni">Kestrel Hill University</span><span class="sep"></span><span class="academy">Alpine Directors Academy</span></div>
  <div class="tag" style="top:31px">Compliance</div>
  <p class="focus-list">Rekrutierung und Nachfolgeplanung<br>Diversität<br>Ethik und Unternehmenskultur</p>
  <div class="law">
    <p class="art">Art. 716a</p>
    <p class="lead"><b>Der Verwaltungsrat</b> hat folgende <b>unübertragbare und unentziehbare</b> Aufgaben:</p>
    <ol>
      <li><span class="n">1.</span><span>die Oberleitung der Gesellschaft und die Erteilung der nötigen Weisungen;</span></li>
      <li><span class="n">2.</span><span>die Festlegung der Organisation;</span></li>
      <li><span class="n">3.</span><span>die Ausgestaltung des Rechnungswesens, der Finanzkontrolle sowie der Finanzplanung, sofern diese für die Führung der Gesellschaft notwendig ist;</span></li>
      <li style="line-height:13.5px"><span class="n">4.</span><span>die <span class="hl">Ernennung und Abberufung der mit der Geschäftsführung und der Vertretung betrauten Personen;</span></span></li>
    </ol>
    <p class="more">…</p>
  </div>
  <p class="pageno">7</p>
  <p class="foot">© Corporate Governance, M. Hausmann-Vogt, 2023</p>
</section>

<section class="slide s7">
  <div class="hex-field" role="img" aria-label="Dezentes Wabenmuster in Hellgrau"></div>
  <div class="brand"><span class="mark"></span><span class="uni">Kestrel Hill University</span><span class="sep"></span><span class="academy">Alpine Directors Academy</span></div>
  <div class="tag" style="top:31px">Compliance</div>
  <h2 class="ttl"><b>TYPISCHE BEISPIELE</b><br><span style="font-weight:400">EINE AUSWAHL</span></h2>
  <ul class="cases">
    <li><i>A</i>Veruntreuung</li><li><i>B</i>Betrug</li><li><i>C</i>Ungetreue Geschäftsbesorgung</li><li><i>D</i>Bestechung</li><li><i>E</i>Unternehmensstrafrecht</li><li><i>F</i>Kartellrecht</li><li><i>G</i>Datenschutz</li><li><i>H</i>Konflikte am Arbeitsplatz</li><li><i>I</i>Weitere Rechtsgebiete</li>
  </ul>
  <svg class="abs" style="left:0;top:0" width="438" height="246" viewBox="0 0 438 246" font-family="Arimo, Arial, sans-serif">
    <defs>
      <radialGradient id="coreFill" cx=".5" cy=".4" r=".6"><stop offset="0" stop-color="#ffd54a"/><stop offset="1" stop-color="#f7bd00"/></radialGradient>
      <radialGradient id="satFill" cx=".4" cy=".35" r=".7"><stop offset="0" stop-color="#ffffff" stop-opacity=".9"/><stop offset="1" stop-color="#d2d2d2" stop-opacity=".85"/></radialGradient>
    </defs>
    <circle cx="279" cy="138" r="66" fill="url(#coreFill)"/>
    <text x="279" y="141" text-anchor="middle" font-size="9" font-weight="700" fill="#fff">Compliance</text>
    <g fill="url(#satFill)" stroke="#e8e8e8" stroke-width="1.2">
      <circle cx="279" cy="71" r="27"/><circle cx="336" cy="108" r="27"/><circle cx="343" cy="174" r="27"/>
      <circle cx="279" cy="203" r="27"/><circle cx="215" cy="174" r="27"/><circle cx="222" cy="108" r="27"/>
    </g>
    <g font-size="5" fill="#444" text-anchor="middle">
      <text x="279" y="73">Aufsichtsrecht</text>
      <text x="336" y="110">Strafrecht</text>
      <text x="343" y="176">Spezialgesetze</text>
      <text x="279" y="202">Policies &amp;</text><text x="279" y="208">Procedures</text>
      <text x="215" y="176">Arbeitsrecht</text>
      <text x="222" y="104">Ausländ.</text><text x="222" y="110">Gesetze</text><text x="222" y="116">(FCPA, GDPR)</text>
    </g>
  </svg>
  <p class="pageno">15</p>
  <p class="foot">© Corporate Governance, M. Hausmann-Vogt, 2022</p>
</section>

<section class="slide s8">
  <p class="kicker">Compliance</p>
  <p class="rel">RELEVANZ</p>
  <p class="sc">STRATEGY AND CULTURE</p>
  <blockquote><span>«</span>You can have all the right strategy in<br>the world; if you don’t have the right<br>culture, you’re dead.<span>»</span></blockquote>
  <p class="by">– Adrian Fellowes, CO-CEO of Northgate Talent</p>
  <p class="pageno">37</p>
  <p class="foot">© Corporate Governance, M. Hausmann-Vogt, 2023</p>
</section>

</body>
</html>
```